Orvex App Form Input Screens - Sleek Clean Design

We have a input form that we would like to transpose into an Orvex App. We have a programmer to do the screens but we need to take this very field heavy form and get it into clean design input screens (We can as many screens as make sense). We want to design to be slick and intuitive. This will be used by young guys who enjoy a gaming atmosphere. But the design has to be easy enough to be completely intuitive to a novice user. The Company likes to do things with Sky Blue colors. Also OK to incorporate burnt orange/yellow (Think glowing sun).

Target Market(s)

18-25 year old males - These guys go door to door and input this data all day

Industry/Entity Type

Solar Energy

Number of Pages Required

5+ page

Font styles to use
Sans Serif

Colors
0355a3
3277b5
85acd3
d0dfed
faa54b
ffc214
f68e4d

Requirements
Must have
• Clean simple sleek Designs - Drop Down Examples. The background and fields have to have distinct colors because these guys will be outside most of the time and if the design is not contrasted enough, it will be hard for them to see.
Nice to have
• Fun ways to incorporate the Glowing Sun Colors (Subtle)
Should not have
• Should not look like Powerpoint

```html
<!DOCTYPE html>
<html lang="en">
<head>
<meta charset="utf-8">
<title>Orvex Solar Site Form</title>
<link href="https://fonts.googleapis.com/css2?family=Roboto+Condensed:wght@400;700&display=swap" rel="stylesheet">
<style>
:root{
  --navy:#0355a3;
  --blue:#3277b5;
  --sky:#85acd3;
  --mist:#d0dfed;
  --tab:#2f74b8;
  --select:#6d9fd3;
  --row-top:#f7f7f7;
  --row-bottom:#ececec;
  --line:#ffffff;
  --divider:#dcdcdc;
  --label:#3e4145;
  --frame:#e6e7e9;
}
*{box-sizing:border-box;margin:0;padding:0}
html,body{width:1200px;height:754px;overflow:hidden;background:var(--frame)}
body{font-family:"Roboto Condensed",Arial,sans-serif;color:var(--label);position:relative}
.stage{position:absolute;left:10px;top:10px;width:1180px;height:728px;
  background:radial-gradient(ellipse at 45% 45%,#e3ecf5 0%,#c4d7ea 45%,#8fb3d7 100%)}
.tab{position:absolute;height:28px;background:linear-gradient(#3a7fc2,#2a6cb0);color:#fff;
  font-size:10.5px;font-weight:700;text-transform:uppercase;letter-spacing:.2px;
  display:flex;align-items:center;justify-content:center;gap:6px}
.tab svg{width:18px;height:18px;fill:none;stroke:#fff;stroke-width:2}
.panel{position:absolute}
.row{height:31.3px;display:flex;align-items:stretch;background:linear-gradient(var(--row-top),var(--row-bottom));
  border-top:1px solid var(--line);font-size:10px}
.cell{display:flex;align-items:center;padding:0 10px;flex:1;white-space:nowrap}
.cell+.cell{border-left:1px solid var(--line)}
.fix{flex:none}
.note{margin-left:auto;font-size:7px}
.choose{margin-left:8px;width:64px;height:17px;border-radius:2px;background:linear-gradient(#7eabd9,#5d92c9);
  color:#fff;font-size:9.5px;display:flex;align-items:center;justify-content:space-between;padding:0 7px;
  box-shadow:0 1px 1px rgba(0,0,0,.15)}
.choose::after{content:"";border-left:4px solid transparent;border-right:4px solid transparent;border-top:5px solid #fff}
.check{display:flex;align-items:center;gap:5px}
.check i{width:8px;height:8px;border:1px solid #9a9a9a;background:#e9e9e9;display:block}
.grid .cell{justify-content:center;padding:0}
.grid .cell.lead{justify-content:flex-start;padding-left:10px;width:125px;flex:none}
.band{height:22px;background:var(--tab);color:#fff;font-size:10px;font-weight:700;text-transform:uppercase;
  display:flex;align-items:center;justify-content:center;gap:5px}
.band svg{width:14px;height:10px;fill:none;stroke:#fff;stroke-width:1.5}
.area{background:linear-gradient(#fbfbfb,#ededed);border-top:1px solid var(--line)}
.area .cell{height:31px}
</style>
</head>
<body>
<div class="stage"></div>

<!-- Column one -->
<div class="tab" style="left:41px;top:41px;width:232px">
  <svg viewBox="0 0 20 20"><path d="M3 10l5 5 9-11" stroke-width="3"/></svg>Record Type</div>
<div class="panel" style="left:31px;top:69px;width:337px">
  <div class="row"><div class="cell" style="gap:18px">
    <span class="check"><i></i>Helivo</span><span class="check"><i></i>Brightway</span>
    <span class="check"><i></i>Toplane</span><span class="check"><i></i>Cash</span><span class="check"><i></i>Other</span>
  </div></div>
</div>

<div class="tab" style="left:41px;top:113px;width:232px">
  <svg viewBox="0 0 20 20" style="fill:#fff;stroke:none"><circle cx="10" cy="6" r="4.5"/><path d="M1 20c0-6 4-8 9-8s9 2 9 8z"/></svg>Customer Information</div>
<div class="panel" style="left:31px;top:141px;width:337px">
  <div class="row"><div class="cell">Who Passed Credit?<span class="note">(For Brightway, this person must be on title)</span></div></div>
  <div class="row"><div class="cell">Name as it Appears on Electric Bill</div></div>
  <div class="row"><div class="cell">Primary Owner (Full Name)</div><div class="cell fix" style="width:126px">On Title<span class="choose">Choose</span></div></div>
  <div class="row"><div class="cell">Email</div></div>
  <div class="row"><div class="cell">Home Phone</div></div>
  <div class="row"><div class="cell">Cell Phone</div></div>
</div>

<div class="tab" style="left:41px;top:342px;width:232px">
  <svg viewBox="0 0 20 20" style="fill:#fff;stroke:none"><circle cx="10" cy="6" r="4.5"/><path d="M1 20c0-6 4-8 9-8s9 2 9 8z"/></svg>Secondary Customer Information</div>
<div class="panel" style="left:31px;top:370px;width:337px">
  <div class="row"><div class="cell">Secondary Owner (Full Name)</div><div class="cell fix" style="width:126px">On Title<span class="choose">Choose</span></div></div>
  <div class="row"><div class="cell">Email</div></div>
  <div class="row"><div class="cell">Home Phone</div></div>
  <div class="row"><div class="cell">Cell Phone</div></div>
  <div class="row"><div class="cell">Installation Address</div></div>
  <div class="row"><div class="cell fix" style="width:148px">City</div><div class="cell fix" style="width:94px">State</div><div class="cell">Zip</div></div>
  <div class="row"><div class="cell">Township taxes paid to</div></div>
  <div class="row"><div class="cell fix" style="width:208px">Does customer have HOA?<span class="choose">Choose</span></div><div class="cell">Name</div></div>
  <div class="row"><div class="cell fix" style="width:208px">HOA Address</div><div class="cell">Phone</div></div>
</div>

<!-- Column two -->
<div class="tab" style="left:390px;top:41px;width:232px">
  <svg viewBox="0 0 20 20"><circle cx="10" cy="10" r="8"/><path d="M10 10l4-4M5 10h1M10 5v1M15 10h-1"/></svg>Utility Information</div>
<div class="panel" style="left:380px;top:69px;width:336px">
  <div class="row"><div class="cell fix" style="width:112px">Utility</div><div class="cell fix" style="width:112px">Account #</div><div class="cell">Meter #</div></div>
  <div class="row"><div class="cell fix" style="width:168px">Usage (Yearly)</div><div class="cell">Meter Location<span class="choose" style="margin-left:auto">Choose</span></div></div>
</div>

<div class="tab" style="left:390px;top:145px;width:232px">
  <svg viewBox="0 0 20 20"><path d="M11 2L6 11h5l-2 7 6-10h-5z" fill="#fff" stroke="none"/><path d="M2 6h2M1 13h2M17 4l1-1M17 15l2 1"/></svg>Electrical Information</div>
<div class="panel" style="left:380px;top:173px;width:336px">
  <div class="row"><div class="cell fix" style="width:182px">Main Breaker Size<span class="choose" style="margin-left:auto">Choose</span></div><div class="cell">Location<span class="choose" style="margin-left:auto">Choose</span></div></div>
  <div class="row"><div class="cell fix" style="width:182px">Main Panel Location<span class="choose" style="margin-left:auto">Choose</span></div><div class="cell">Sub Location<span class="choose" style="margin-left:auto">Choose</span></div></div>
  <div class="row"><div class="cell">Inverter Location (Next to Meter)</div></div>
  <div class="row"><div class="cell">Consultant</div></div>
  <div class="row"><div class="cell">Phone</div></div>
  <div class="row"><div class="cell">Date</div></div>
  <div class="row"><div class="cell">Tentative Installation Date</div></div>
</div>

<div class="tab" style="left:390px;top:406px;width:232px">
  <svg viewBox="0 0 20 20"><path d="M1 5h4l8 10h5M1 15h4l8-10h5M15 2l3 3-3 3M15 12l3 3-3 3"/></svg>System Details</div>
<div class="panel" style="left:380px;top:434px;width:336px">
  <div class="row"><div class="cell">Total System Size (kW)</div></div>
  <div class="row"><div class="cell">Panel Type</div></div>
  <div class="row"><div class="cell">Is it ok with customer to move vents/pipe/fans as needed?<span class="choose" style="margin-left:auto">Choose</span></div></div>
</div>

<!-- Column three -->
<div class="tab" style="left:738px;top:41px;width:232px">
  <svg viewBox="0 0 20 20"><path d="M1 15l7-8 4 4 2-3 5 6"/></svg>Roof Mount</div>
<div class="panel grid" style="left:729px;top:69px;width:440px">
  <div class="row"><div class="cell lead"></div><div class="cell">Main</div><div class="cell">Additional</div><div class="cell">Additional</div><div class="cell">Additional</div></div>
  <div class="row"><div class="cell lead">Roof Type</div><div class="cell"></div><div class="cell"></div><div class="cell"></div><div class="cell"></div></div>
  <div class="row"><div class="cell lead"># of Layers</div><div class="cell"></div><div class="cell"></div><div class="cell"></div><div class="cell"></div></div>
  <div class="row"><div class="cell lead">Attic Access?</div><div class="cell"></div><div class="cell"></div><div class="cell"></div><div class="cell"></div></div>
  <div class="row"><div class="cell lead">Rafter Size</div><div class="cell"></div><div class="cell"></div><div class="cell"></div><div class="cell"></div></div>
  <div class="row"><div class="cell lead">Rafter Spacing</div><div class="cell"></div><div class="cell"></div><div class="cell"></div><div class="cell"></div></div>
  <div class="row"><div class="cell lead">Horizontal Span</div><div class="cell"></div><div class="cell"></div><div class="cell"></div><div class="cell"></div></div>
  <div class="row"><div class="cell lead">Trench Length</div><div class="cell"></div><div class="cell"></div><div class="cell"></div><div class="cell"></div></div>
  <div class="band"><svg viewBox="0 0 14 10"><path d="M1 7h12M3 7c0-3 2-4 4-4s4 1 4 4"/></svg>Ground Mount</div>
  <div class="row"><div class="cell lead">Location of Array</div><div class="cell"></div><div class="cell"></div><div class="cell"></div><div class="cell"></div></div>
  <div class="row"><div class="cell lead">Trench Length</div><div class="cell"></div><div class="cell"></div><div class="cell"></div><div class="cell"></div></div>
</div>

<div class="tab" style="left:738px;top:418px;width:232px">
  <svg viewBox="0 0 20 20"><rect x="4" y="4" width="12" height="15" fill="#fff" stroke="none"/><rect x="7" y="1.5" width="6" height="4" fill="#fff"/></svg>Special Instructions from Homeowner</div>
<div class="panel area" style="left:729px;top:446px;width:440px;height:94px"></div>

<div class="tab" style="left:738px;top:553px;width:232px">
  <svg viewBox="0 0 20 20"><path d="M2 2l16 16M18 2L2 18M14 2l4 4"/></svg>Measure Information</div>
<div class="panel" style="left:729px;top:581px;width:440px">
  <div class="row"><div class="cell fix" style="width:220px">Do Trees Need to be Cut?<span class="choose" style="margin-left:auto">Choose</span></div><div class="cell">When?<span class="note">(New site survey will be required)</span></div></div>
  <div class="area" style="height:94px"><div class="cell">Instructions for Measure / Installation Crew</div></div>
</div>
</body>
</html>
```